Website Groeien met Pixelpost Ads Course

I would like to have a website built for Pixelpost Marketing course. in this course you learn everything about Pixelpost and Snapvista marketing.

The example websites you can use are: https://karvimo.example/, https://pakketschool.example/

I have some landingpages that you van use as inspiration:
https://groeienmetpixelpostads.trechterbouw.example/aanmelden-gratis-training
https://groeienmetpixelpostads.trechterbouw.example/squeeze-pagequdvbiyz

I would like a quick, clear website.

I am very curious what you make of it.

I want thate the pixelpost color are used

If you need more information, send me a message please

Target Market(s)

Marketing managers, entrepreneurs,

Industry/Entity Type

Digital Marketing

Coding

Coded - Design and coding required

Number of Pages Required

4 page

Font styles to use
Sans Serif

Colors

Designer to choose colors to be used in the design.

Requirements
Must have
• Update and price page
Nice to have
• -
Should not have
• -

```html
<!DOCTYPE html>
<html lang="nl">
<head>
<meta charset="utf-8">
<title>Groeien met Pixelpost Ads</title>
<link href="https://fonts.googleapis.com/css2?family=Montserrat:wght@400;500;600;700&display=swap" rel="stylesheet">
<style>
:root{
  --gold:#d9a03a;
  --gold-soft:#e9cf9d;
  --blue:#2f66ab;
  --blue-deep:#1d3f6e;
  --navy:#16243a;
  --ink:#222;
  --muted:#444;
  --white:#fff;
}
*{margin:0;padding:0;box-sizing:border-box}
html,body{width:1200px;height:3934px;overflow:hidden}
body{font-family:'Montserrat',sans-serif;color:var(--ink);background:var(--white);position:relative}
.abs{position:absolute}
.btn{position:absolute;display:flex;align-items:center;gap:12px;background:var(--gold);color:var(--white);border-radius:26px;font-size:16px;font-weight:500;text-transform:uppercase;padding:0 20px;text-decoration:none}
.btn svg{width:22px;height:22px}
/* header */
.site-header{position:absolute;left:0;top:0;width:1200px;height:144px;background:var(--white)}
.brand{position:absolute;display:flex;align-items:center;gap:8px;font-weight:600;color:var(--blue);font-size:16px;line-height:1.2}
.brand .dot{width:22px;height:22px;background:var(--gold);border-radius:50%;flex:none}
.nav{position:absolute;left:311px;top:86px;display:flex;gap:0}
.nav a{font-size:18px;color:var(--ink);text-decoration:none;text-transform:uppercase;margin-right:30px}
.nav a.active{color:var(--gold)}
/* hero */
.hero{position:absolute;left:0;top:144px;width:1200px;height:580px;overflow:hidden}
.hero-bg{position:absolute;inset:0;background:linear-gradient(120deg,#1d3350,#2a4a70 45%,#1a2e4a)}
.hero-photo{position:absolute;left:142px;top:18px;width:370px;height:470px;border-radius:50%;background:radial-gradient(circle at 45% 45%,#f3f1ee,#d9d6d2 70%,#c7c3be)}
.hero-chair{position:absolute;left:0;top:360px;width:330px;height:220px;background:linear-gradient(160deg,#f2b423,#d8901a)}
.hero-copy{position:absolute;left:538px;top:150px;width:580px}
.hero-title{color:var(--white);font-size:26px;line-height:44px;font-weight:500}
.hero-copy .btn{position:relative;display:inline-flex;height:50px;margin-top:18px;padding:0 16px}
.dots{position:absolute;left:1143px;top:236px;display:flex;flex-direction:column;gap:12px}
.dots span{width:10px;height:10px;border-radius:50%;background:var(--white)}
.dots span.on{background:var(--gold)}
/* intro */
.intro-title{position:absolute;left:52px;top:803px;font-size:38px;font-weight:500;line-height:56px}
.benefits{position:absolute;left:55px;top:955px;list-style:none}
.benefits li{display:flex;gap:22px;font-size:16px;line-height:36.5px;color:var(--ink)}
.benefits li svg{flex:none;width:24px;height:24px;margin-top:6px}
.benefits em{font-style:normal;color:var(--gold)}
.free-note{position:absolute;left:100px;top:1144px;width:670px;font-size:16.5px;line-height:36px}
.free-note strong{color:var(--gold);font-weight:500}
.note{position:absolute;left:58px;top:1280px;width:740px;font-size:16.5px;line-height:36px;display:flex;gap:14px;font-weight:500}
.note b{color:var(--gold);font-weight:500}
.intro-photo{position:absolute;left:829px;top:864px;width:330px;height:386px;border:8px solid var(--gold);background:linear-gradient(180deg,#e4e2de,#b9b3ab 60%,#8d7f70)}
/* discover */
.discover{position:absolute;left:0;top:1427px;width:1200px;height:617px;background:linear-gradient(135deg,#3c6dab,#2f62a2 50%,#3a6dae)}
.discover h2{position:absolute;left:0;top:52px;width:1200px;text-align:center;color:var(--white);font-size:40px;font-weight:500;line-height:56px}
.feature{position:absolute;top:203px;width:290px;text-align:center;color:var(--white);font-size:22px;line-height:33px}
.feature .art{width:250px;height:250px;margin:0 auto 42px;border-radius:50%;border:6px solid var(--gold);background:radial-gradient(circle,#ffffff 55%,#eef2f7)}
/* about */
.about-photo{position:absolute;left:100px;top:2126px;width:352px;height:374px;background:linear-gradient(180deg,#e8e6e2,#c9c2b8 55%,#9b8468);box-shadow:10px 10px 0 var(--blue-deep)}
.about h2{position:absolute;left:521px;top:2118px;font-size:38px;font-weight:500}
.about p{position:absolute;left:521px;top:2183px;width:563px;font-size:17px;line-height:35.2px;text-align:justify;color:var(--muted)}
/* signup */
.signup{position:absolute;left:0;top:2582px;width:1200px;height:350px;background:var(--blue)}
.signup-photo{position:absolute;left:628px;top:0;width:572px;height:350px;background:linear-gradient(90deg,#2f66ab,#1e2c44 30%,#2a3a55 70%,#3b70b0)}
.signup h2{position:absolute;left:111px;top:82px;color:var(--white);font-size:37px;font-weight:400}
.signup h2 strong{font-weight:600}
.signup p{position:absolute;left:111px;top:146px;color:var(--white);font-size:24px}
/* pricing */
.pricing-title{position:absolute;left:0;top:2990px;width:1200px;text-align:center;font-size:40px;font-weight:500}
.pricing-title span{color:var(--blue)}
.plan{position:absolute;top:3099px;width:306px;height:466px;border:3px solid #d4dcea;border-radius:4px;background:var(--white);box-shadow:0 3px 8px rgba(0,0,0,.12)}
.plan::after{content:"";position:absolute;left:3px;right:3px;bottom:-3px;height:9px;background:var(--gold);border-radius:4px 4px 0 0}
.plan h3{margin-top:26px;text-align:center;font-size:22px;font-weight:500}
.plan .price{text-align:center;font-size:46px;font-weight:700;color:var(--blue);margin-top:8px}
.plan .art{width:136px;height:106px;margin:14px auto 0;border-radius:10px;background:linear-gradient(135deg,#e7eef8,#f6e7cc)}
.plan ul{list-style:none;margin:30px 0 0 16px}
.plan li{display:flex;gap:18px;font-size:16px;line-height:27px;color:var(--muted);margin-bottom:16px;width:275px}
.plan li svg{flex:none;width:28px;height:28px;margin-top:4px}
/* footer */
.site-footer{position:absolute;left:0;top:3628px;width:1200px;height:306px;background:linear-gradient(135deg,#2f62a4,#2a5c9f)}
.site-footer .brand{left:536px;top:22px;width:128px;height:122px;background:var(--white);flex-direction:column;justify-content:center;text-align:center;font-size:14px;gap:6px;padding:6px}
.footer-nav{position:absolute;left:0;top:164px;width:1200px;display:flex;justify-content:center;gap:30px}
.footer-nav a{color:var(--white);font-size:18px;text-decoration:none;text-transform:uppercase}
.social{position:absolute;left:580px;top:3840px;width:40px;height:40px;border:2px solid var(--white);border-radius:50%}
.social span{position:absolute;left:11px;top:11px;width:14px;height:14px;background:var(--white);border-radius:2px}
.copyright{position:absolute;left:0;top:3896px;width:1200px;text-align:center;color:var(--white);font-size:19px}
</style>
</head>
<body>
<svg width="0" height="0" style="position:absolute">
  <defs>
    <symbol id="arrow-circle" viewBox="0 0 24 24"><circle cx="12" cy="12" r="11" fill="currentColor"/><path d="M6.5 12h10M12.5 7.5 17 12l-4.5 4.5" stroke="#fff" stroke-width="2.6" fill="none" stroke-linecap="round" stroke-linejoin="round"/></symbol>
    <symbol id="arrow-white" viewBox="0 0 24 24"><circle cx="12" cy="12" r="11" fill="#fff"/><path d="M6.5 12h10M12.5 7.5 17 12l-4.5 4.5" stroke="#d9a03a" stroke-width="2.6" fill="none" stroke-linecap="round" stroke-linejoin="round"/></symbol>
    <symbol id="tick" viewBox="0 0 28 28"><path d="M3 15l7 7L25 5" stroke="#2f66ab" stroke-width="4" fill="none" stroke-linecap="round" stroke-linejoin="round"/></symbol>
  </defs>
</svg>

<header class="site-header">
  <div class="brand" style="left:115px;top:40px;width:150px"><span class="dot"></span>Groeien met Pixelpost Ads</div>
  <nav class="nav">
    <a class="active" href="#">Features</a>
    <a href="#">Extra Services</a>
    <a href="#">Prijzen</a>
    <a href="#">Academy</a>
    <a href="#">Updates</a>
    <a href="#">Dashboard</a>
  </nav>
  <a class="btn" href="#" style="left:916px;top:16px;height:50px;font-size:16px;padding:0 14px;gap:8px">Get Started<svg><use href="#arrow-white"/></svg></a>
</header>

<section class="hero">
  <div class="hero-bg" role="img" aria-label="Dark textured surface background"></div>
  <div class="hero-chair" role="img" aria-label="Yellow chair"></div>
  <div class="hero-photo" role="img" aria-label="Hands typing on a laptop on a desk"></div>
  <div class="hero-copy">
    <h1 class="hero-title">GRATIS TRAINING: Leer Hoe Je Pixelpost en Snapvista Advertenties Succesvol kunt inzetten voor je bedrijf! &nbsp;(3 geheimen)</h1>
    <a class="btn" href="#">Register Now<svg><use href="#arrow-white"/></svg></a>
  </div>
  <div class="dots"><span></span><span></span><span class="on"></span></div>
  <svg class="abs" style="left:0;top:470px" width="1200" height="110" viewBox="0 0 1200 110" preserveAspectRatio="none">
    <path d="M0 40 C120 30 300 10 400 95 C520 20 650 35 760 60 C900 90 1050 40 1200 20 L1200 110 L0 110 Z" fill="#e9cf9d"/>
    <path d="M0 60 C120 50 300 30 400 110 C520 40 650 55 760 80 C900 110 1050 60 1200 42 L1200 110 L0 110 Z" fill="#fff"/>
  </svg>
</section>

<section class="intro">
  <h2 class="intro-title">During This Unique<br>Online Training Discover You</h2>
  <ul class="benefits">
    <li><svg style="color:var(--gold)"><use href="#arrow-circle"/></svg>How you can successfully use Pixelpost and Snapvista Ads for your company</li>
    <li><svg style="color:var(--gold)"><use href="#arrow-circle"/></svg>How you can see exactly what your competitors are doing online</li>
    <li><svg style="color:var(--gold)"><use href="#arrow-circle"/></svg>How you can convert website visitors who do not convert to customers</li>
    <li><svg style="color:var(--gold)"><use href="#arrow-circle"/></svg><span>How you <em>can grow</em> your turnover by 20% without having to spend<br>&nbsp;more than 1 hour a day on it.</span></li>
  </ul>
  <p class="free-note"><strong>The training is 100% FREE .</strong> You do not need any prior knowledge to attend the training, everything is explained step by step so that you can achieve success.</p>
  <p class="note"><b>Note:</b><span>The software that we use has only a certain number of places available. Click on the button above to claim your place</span></p>
  <div class="intro-photo" role="img" aria-label="Trainer presenting at a lectern to a seated audience"></div>
</section>

<section class="discover">
  <h2>DURING THIS UNIQUE FREE<br>TRAINING YOU DISCOVER:</h2>
  <div class="feature" style="left:146px"><div class="art" role="img" aria-label="Illustration of growth chart and money"></div>How You Pixelpost and Snapvista ads Successful can bet</div>
  <div class="feature" style="left:482px"><div class="art" role="img" aria-label="Illustration of a trophy bursting from a screen"></div>The value that a good mentor can have for you</div>
  <div class="feature" style="left:793px"><div class="art" role="img" aria-label="Illustration of a thinking person with question marks"></div>How you can convert people who have left the website into customers</div>
</section>

<section class="about">
  <div class="about-photo" role="img" aria-label="Trainer giving a workshop to a full room"></div>
  <h2>About Daan Verhoef</h2>
  <p>Daan Verhoef is an online entrepreneur and is seen as an authority in the field of Pixelpost and Snapvista Ads . Daan has built up an incredibly beautiful company in 2 years, all through the use of Pixelpost and Snapvista Ads . Daan Verhoef, for example, manages several Web shops and has Online Marketing Agency that specializes in Pixelpost and Snapvista advertisements.</p>
  <a class="btn" href="#" style="left:521px;top:2464px;height:48px;font-size:16px;padding:0 14px;gap:10px">Read More<svg><use href="#arrow-white"/></svg></a>
</section>

<section class="signup">
  <div class="signup-photo" role="img" aria-label="Businessman holding a tablet with floating digital icons"></div>
  <h2>Sign up <strong>NOW</strong> for <strong>FREE TRAINING</strong></h2>
  <p>Click on the button below to sign up</p>
  <a class="btn" href="#" style="left:113px;top:198px;height:50px;font-size:16px;padding:0 20px;gap:22px">Register Now<svg><use href="#arrow-white"/></svg></a>
</section>

<section class="pricing">
  <h2 class="pricing-title">Our <span>Pricing</span></h2>
  <div class="plan" style="left:113px">
    <h3>STARTER</h3><div class="price">$32</div>
    <div class="art" role="img" aria-label="Illustration of analytics chart with magnifier"></div>
    <ul>
      <li><svg><use href="#tick"/></svg>Sed ut perspiciatis unde omnis iste natus error sit</li>
      <li><svg><use href="#tick"/></svg>Lorem ipsum dolor sit amet, consectetur cing elit, sed.</li>
    </ul>
  </div>
  <div class="plan" style="left:449px">
    <h3>ADVANCED</h3><div class="price">$37</div>
    <div class="art" role="img" aria-label="Illustration of marketing dashboard"></div>
    <ul>
      <li><svg><use href="#tick"/></svg>Sed ut perspiciatis unde omnis iste natus error sit</li>
      <li><svg><use href="#tick"/></svg>Lorem ipsum dolor sit amet, consectetur cing elit, sed.</li>
    </ul>
  </div>
  <div class="plan" style="left:784px">
    <h3>PRO</h3><div class="price">$75</div>
    <div class="art" role="img" aria-label="Illustration of mobile marketing"></div>
    <ul>
      <li><svg><use href="#tick"/></svg>Sed ut perspiciatis unde omnis iste natus error sit</li>
      <li><svg><use href="#tick"/></svg>Lorem ipsum dolor sit amet, consectetur cing elit, sed.</li>
    </ul>
  </div>
</section>

<footer class="site-footer">
  <div class="brand"><span class="dot"></span>Groeien met Pixelpost Ads</div>
  <nav class="footer-nav">
    <a href="#">Features</a><a href="#">Extra Services</a><a href="#">Prijzen</a><a href="#">Academy</a><a href="#">Updates</a><a href="#">Dashboard</a>
  </nav>
</footer>
<div class="social" aria-label="Pixelpost"><span></span></div>
<p class="copyright">Copyrights 2019. All rights reserved</p>
</body>
</html>
```